Marisol Quandt Designs

- Interior design consultant
- Want a monogram/logo at the top within a circle similar to tovalenstudio.com.au
- Want the colors, font, theme, layout to be similar to tovalenstudio.com.au
- Monogram possibly in the gold circle/leaf thing as visible on the attached pictures, maybe a Marisol Quandt with a backwards "E" within a circle
- Black background, white writing
- 1 side an enlarge logo with nothing else, other side to have a small logo at top with company name, mobile and email below

Industry/Entity Type

It Company

Contact Information for Business Card

Company name: Marisol Quandt Interiors
Mobile: 0461 385 519
Email: marisolquandt@mailvista.example

Colors
000000
ffffff

```html
<!DOCTYPE html>
<html lang="en">
<head>
<meta charset="utf-8">
<title>Marisol Quandt Interiors — Business Card</title>
<link rel="stylesheet" href="https://fonts.googleapis.com/css2?family=Cinzel:wght@400&family=Cormorant+Garamond:wght@500&display=swap">
<style>
  :root {
    --card-black: #000000;
    --ink-white: #ffffff;
    --backdrop: #9a5236;
  }
  * { margin: 0; padding: 0; box-sizing: border-box; }
  html, body { width: 1200px; height: 960px; overflow: hidden; }
  body {
    background: var(--backdrop);
    display: flex;
    flex-direction: column;
    align-items: center;
    justify-content: center;
    gap: 54px;
  }
  .card {
    position: relative;
    width: 700px;
    height: 400px;
    background: var(--card-black);
    border-radius: 28px;
    color: var(--ink-white);
    box-shadow: 0 10px 24px rgba(0,0,0,0.35);
  }
  .brand-ring {
    position: absolute;
    border: 9px solid var(--ink-white);
    border-radius: 50%;
    display: flex;
    flex-direction: column;
    align-items: center;
    justify-content: center;
    font-family: "Cinzel", serif;
    font-weight: 400;
    color: var(--ink-white);
    line-height: 1.15;
    text-align: center;
  }
  .card-front .brand-ring {
    width: 250px; height: 250px;
    left: 225px; top: 75px;
    font-size: 30px;
  }
  .card-back .brand-ring {
    width: 200px; height: 200px;
    left: 60px; top: 100px;
    font-size: 24px;
    border-width: 8px;
  }
  .company-name {
    position: absolute;
    left: 300px;
    right: 34px;
    top: 150px;
    text-align: right;
    font-family: "Cinzel", serif;
    font-size: 25px;
    letter-spacing: 0.04em;
    white-space: nowrap;
  }
  .contact-list {
    position: absolute;
    right: 34px;
    top: 196px;
    list-style: none;
    font-family: "Cormorant Garamond", serif;
    font-weight: 500;
    font-size: 17px;
  }
  .contact-item {
    display: flex;
    align-items: center;
    justify-content: flex-end;
    gap: 12px;
    height: 26px;
  }
  .contact-icon { width: 14px; height: 14px; }
</style>
</head>
<body>
  <section class="card card-front" aria-label="Card front">
    <div class="brand-ring"><span>Marisol</span><span>Quandt</span></div>
  </section>

  <section class="card card-back" aria-label="Card back">
    <div class="brand-ring"><span>Marisol</span><span>Quandt</span></div>
    <h1 class="company-name">Marisol Quandt Interiors</h1>
    <ul class="contact-list">
      <li class="contact-item">
        <span>0461 385 519</span>
        <svg class="contact-icon" viewBox="0 0 14 14" aria-hidden="true">
          <rect x="3.5" y="1" width="7" height="12" rx="1.5" fill="none" stroke="#ffffff" stroke-width="1.4"/>
          <circle cx="7" cy="10.8" r="0.8" fill="#ffffff"/>
        </svg>
      </li>
      <li class="contact-item">
        <span>marisolquandt@mailvista.example</span>
        <svg class="contact-icon" viewBox="0 0 14 14" aria-hidden="true">
          <rect x="1" y="3" width="12" height="8.5" fill="#ffffff"/>
          <path d="M1 3 L7 8 L13 3" fill="none" stroke="#000000" stroke-width="1.2"/>
        </svg>
      </li>
    </ul>
  </section>
</body>
</html>
```